Special Educational Conference Poster

Looking for a poster that I can use electronically more than anything - to post on Chatterbook \ social media. Should be bold, eye catching, and within our brand colors.

3rd Annual Young Learners Beyond Limits Summit
Featuring Dr. Martin Ellery
Lighting the Way: Growing Courage, Drive, and Grit in Every Young Learner Who Thinks Differently

Friday, May 10, 2019, 9am - 3pm

The Linden Grove Academy at Fenwick opens our campus to teachers, parents, and practitioners from the Delaware Valley to learn together on how to support the extraordinary students in our lives. The conference runs from 9am - 3pm and lunch is included. This event is free and open to the public, but registration is required.

Link to registration: https://www.lindengroveacad.org/admissions/admissions-visit-and-events

```html
<!DOCTYPE html>
<html lang="en">
<head>
<meta charset="utf-8">
<title>Young Learners Beyond Limits Summit</title>
<link rel="stylesheet" href="https://fonts.googleapis.com/css2?family=Montserrat:wght@300;600;700;800&family=Oswald:wght@500;600&family=Open+Sans:wght@400;600&display=swap">
<style>
:root{
  --navy:#1f4466;
  --navy-deep:#183a5a;
  --gold:#e3b718;
  --white:#ffffff;
  --panel:#ececec;
  --ink:#222222;
  --backdrop:#6b6b6b;
}
*{margin:0;padding:0;box-sizing:border-box}
html,body{width:1200px;height:1200px;overflow:hidden;background:var(--backdrop)}
.flyer{position:absolute;left:170px;top:40px;width:860px;height:1120px;background:var(--white);overflow:hidden;box-shadow:0 10px 30px rgba(0,0,0,.35)}
.flyer-shapes{position:absolute;inset:0}
.brand{position:absolute;left:36px;top:34px;display:flex;align-items:center;gap:10px;font-family:'Montserrat',sans-serif;font-weight:700;font-size:22px;line-height:1.1;color:var(--navy-deep);letter-spacing:.5px}
.brand-mark{width:14px;height:14px;border-radius:50%;background:var(--navy-deep);flex:none}
.headline{position:absolute;left:44px;top:560px;width:440px;color:var(--white)}
.headline-kicker{font-family:'Oswald',sans-serif;font-weight:600;font-size:72px;line-height:1;color:var(--gold);letter-spacing:1px}
.headline-title{font-family:'Montserrat',sans-serif;font-weight:300;font-size:38px;line-height:1.1;margin-top:6px;letter-spacing:1px}
.headline-sub{font-family:'Montserrat',sans-serif;font-weight:800;font-size:30px;line-height:1.1;letter-spacing:1px}
.feature{position:absolute;left:44px;top:800px;width:420px;font-family:'Montserrat',sans-serif;color:var(--navy)}
.feature-speaker{font-weight:700;font-size:23px;line-height:1.25}
.feature-talk{font-weight:700;font-size:22px;line-height:1.25;margin-top:4px}
.feature-desc{font-family:'Open Sans',sans-serif;font-weight:600;font-size:15px;color:var(--ink);line-height:1.35;margin-top:2px}
.date-box{position:absolute;left:40px;top:902px;width:360px;height:96px;background:var(--gold);border-radius:22px;padding:10px 24px;font-family:'Oswald',sans-serif}
.date-day{font-size:48px;font-weight:600;line-height:1;color:var(--navy)}
.date-time{font-size:30px;font-weight:600;line-height:1.1;color:#111}
.about{position:absolute;left:502px;top:706px;width:330px;font-family:'Open Sans',sans-serif;font-size:14px;line-height:1.5;color:var(--ink);text-align:justify}
.registration{position:absolute;left:0;right:0;top:1052px;text-align:center}
.registration-label{font-family:'Oswald',sans-serif;font-weight:600;font-size:24px;line-height:1.2;color:var(--gold);letter-spacing:.5px}
.registration-url{font-family:'Open Sans',sans-serif;font-weight:600;font-size:17px;line-height:1.3;color:var(--white);margin-top:4px}
</style>
</head>
<body>
<main class="flyer">
  <svg class="flyer-shapes" width="860" height="1120" viewBox="0 0 860 1120">
    <defs>
      <linearGradient id="photo-tone" x1="0" y1="0" x2="1" y2="1">
        <stop offset="0" stop-color="#cfd6cf"/>
        <stop offset=".45" stop-color="#a8b9a4"/>
        <stop offset=".7" stop-color="#d9a48e"/>
        <stop offset="1" stop-color="#b86c6c"/>
      </linearGradient>
      <linearGradient id="portrait-tone" x1="0" y1="0" x2="0" y2="1">
        <stop offset="0" stop-color="#d4e3ee"/>
        <stop offset=".6" stop-color="#c9a48f"/>
        <stop offset="1" stop-color="#23324a"/>
      </linearGradient>
    </defs>
    <rect class="hero-photo" x="0" y="0" width="860" height="560" fill="url(#photo-tone)" role="img" aria-label="Photo of cheerful schoolchildren giving a thumbs up in a classroom"/>
    <rect x="480" y="480" width="380" height="480" fill="var(--panel)"/>
    <path d="M0,470 Q420,420 860,290 L860,310 Q420,440 0,492 Z" fill="var(--gold)"/>
    <path d="M0,490 Q420,438 860,308 L860,600 Q450,700 0,800 Z" fill="var(--navy)"/>
    <path d="M0,1060 Q500,1010 860,900 L860,916 Q500,1026 0,1076 Z" fill="var(--gold)"/>
    <path d="M0,1076 Q500,1026 860,916 L860,1120 L0,1120 Z" fill="var(--navy-deep)"/>
    <circle cx="640" cy="420" r="154" fill="var(--gold)"/>
    <circle class="speaker-photo" cx="640" cy="420" r="146" fill="url(#portrait-tone)" role="img" aria-label="Portrait photo of the featured speaker"/>
  </svg>

  <div class="brand"><span class="brand-mark"></span><span>The Linden Grove Academy<br>at Fenwick</span></div>

  <h1 class="headline">
    <div class="headline-kicker">3RD ANNUAL</div>
    <div class="headline-title">YOUNG LEARNERS</div>
    <div class="headline-sub">BEYOND LIMITS<br>SUMMIT</div>
  </h1>

  <section class="feature">
    <p class="feature-speaker">Featuring Dr. Martin Ellery</p>
    <p class="feature-talk">Lighting the Way:</p>
    <p class="feature-desc">Growing Courage, Drive, and Grit in Every Young Learner Who Thinks Differently</p>
  </section>

  <div class="date-box">
    <div class="date-day">MAY 10, 2019</div>
    <div class="date-time">FRIDAY, 9AM - 3PM</div>
  </div>

  <p class="about">The Linden Grove Academy at Fenwick opens our campus to teachers, parents, and practitioners from the Delaware Valley to learn together on how to support the extraordinary students in our lives. The conference runs from 9am - 3pm and lunch is included. This event is free and open to the public, but registration is required.</p>

  <footer class="registration">
    <div class="registration-label">LINK TO REGISTRATION:</div>
    <div class="registration-url">https://www.lindengroveacad.org/admissions/admissions-visit-and-events</div>
  </footer>
</main>
</body>
</html>
```